Business Card Design Project

Business is web based; no retail location. Business card needs to direct potential customers to our website.

Target Market(s)

Parents, Adult Fans of Vantri

Industry/Entity Type

Retail

Requirements
Must have
• Email Address
Website Address
Should not have
• Telephone Number

```html
<!DOCTYPE html>
<html lang="en">
<head>
<meta charset="utf-8">
<title>Harbor Town Blocks – Business Card</title>
<link rel="stylesheet" href="https://fonts.googleapis.com/css2?family=Roboto:wght@400;500;900&display=swap">
<style>
  :root {
    --page-bg: #1c1c1e;
    --card-white: #f4f4f4;
    --card-shade: #dcdcdc;
    --brick-red: #c8161d;
    --band-red: #9b1418;
    --band-blue: #2f6fe6;
    --ink: #3f4147;
    --ink-soft: #5a5d63;
    --divider: #8c8f95;
  }
  html, body {
    margin: 0;
    width: 1200px;
    height: 984px;
    overflow: hidden;
    background: var(--page-bg);
    font-family: "Roboto", Arial, sans-serif;
  }
  .canvas {
    position: relative;
    width: 1200px;
    height: 984px;
  }
  .card {
    position: absolute;
    left: 210px;
    width: 780px;
    height: 446px;
    border-radius: 30px;
    overflow: hidden;
    background: var(--card-white);
  }
  .card--back { top: 30px; }
  .card--front { top: 508px; }
  .card__texture {
    position: absolute;
    inset: 0;
    background: radial-gradient(ellipse at 45% 40%, #fbfbfb 0%, var(--card-white) 45%, var(--card-shade) 100%);
  }
  .card__band {
    position: absolute;
    left: 0;
    bottom: 0;
    width: 100%;
    height: 120px;
  }
  .brand {
    position: absolute;
    display: flex;
    align-items: center;
    gap: 14px;
  }
  .brand__mark {
    width: 34px;
    height: 34px;
    background: var(--brick-red);
    flex: none;
  }
  .brand__name {
    font-weight: 900;
    color: var(--brick-red);
    line-height: 1.02;
  }
  .card--back .brand {
    left: 0;
    right: 0;
    top: 120px;
    justify-content: center;
  }
  .card--back .brand__name { font-size: 54px; }
  .card--front .brand {
    left: 70px;
    top: 150px;
  }
  .card--front .brand__name { font-size: 44px; }
  .card__divider {
    position: absolute;
    left: 420px;
    top: 90px;
    width: 2px;
    height: 250px;
    background: linear-gradient(var(--card-white), var(--divider), var(--card-white));
  }
  .contact {
    position: absolute;
    left: 460px;
    top: 130px;
    width: 300px;
    color: var(--ink);
  }
  .contact__name {
    margin: 0;
    font-size: 34px;
    font-weight: 900;
    color: var(--ink);
  }
  .contact__role {
    margin: 2px 0 26px;
    font-size: 16px;
    color: var(--ink-soft);
  }
  .contact__list {
    list-style: none;
    margin: 0;
    padding: 0;
    font-size: 20px;
    line-height: 1.35;
  }
  .contact__item {
    display: flex;
    gap: 14px;
    margin-bottom: 8px;
    white-space: nowrap;
  }
  .contact__icon {
    width: 18px;
    height: 18px;
    margin-top: 4px;
    flex: none;
    fill: var(--ink);
  }
</style>
</head>
<body>
<main class="canvas">

  <section class="card card--back" aria-label="Business card back">
    <div class="card__texture" role="img" aria-label="Background of stacked white toy bricks"></div>
    <svg class="card__band" viewBox="0 0 780 120" preserveAspectRatio="none" aria-hidden="true">
      <path d="M0 95 Q390 40 780 0 L780 120 L0 120 Z" fill="var(--band-blue)"/>
      <path d="M0 90 Q390 35 780 -5 L780 3 Q390 43 0 98 Z" fill="var(--band-red)"/>
    </svg>
    <div class="brand">
      <span class="brand__mark" aria-hidden="true"></span>
      <span class="brand__name">Harbor Town<br>Blocks</span>
    </div>
  </section>

  <section class="card card--front" aria-label="Business card front">
    <div class="card__texture" role="img" aria-label="Background of stacked white toy bricks"></div>
    <div class="brand">
      <span class="brand__mark" aria-hidden="true"></span>
      <span class="brand__name">Harbor Town<br>Blocks</span>
    </div>
    <div class="card__divider" aria-hidden="true"></div>
    <div class="contact">
      <h1 class="contact__name">Marcus Ellery</h1>
      <p class="contact__role">manager</p>
      <ul class="contact__list">
        <li class="contact__item">
          <svg class="contact__icon" viewBox="0 0 16 16" aria-hidden="true"><rect x="1" y="3" width="14" height="10" rx="1"/><path d="M1.5 3.5 L8 9 L14.5 3.5" stroke="var(--card-white)" stroke-width="1.4" fill="none"/></svg>
          <span>hello@harbortownblocks.com</span>
        </li>
        <li class="contact__item">
          <svg class="contact__icon" viewBox="0 0 16 16" aria-hidden="true"><circle cx="8" cy="8" r="7"/><path d="M1 8 H15 M8 1 Q4 8 8 15 M8 1 Q12 8 8 15" stroke="var(--card-white)" stroke-width="1.2" fill="none"/></svg>
          <span>www.harbortownblocks.com</span>
        </li>
      </ul>
    </div>
  </section>

</main>
</body>
</html>
```